Meridian Rest Supply Needs Business Card

Looking for a very nice looking business card. Creative but not extravagant. We sell beds and pillows across the U.S. and need something professional but catchy. I have attached the logo.

Name : Dale Fenwick
Title : President
Phone : (800) 417-2964
Email: sleep@quorvana.com
Website: www.quorvana.com

Can be single-sided or double-sided
horizontal or vertical

Can use Blues/Greys

Target Market(s)

Mass Market

Industry/Entity Type

Retail

Contact Information for Business Card

Name : Dale Fenwick
Title : President
Phone : (800) 417-2964
Email: sleep@quorvana.com
Website: www.quorvana.com

Requirements
Must have
• Clean, Modern, Smooth
• Can use Blues/Greys
• On the other side without the information - have something simple like www.quorvana.com or our logo
Nice to have
• Surprise me
Should not have
• Nothing crazy, nothing cluttered

```html
<!DOCTYPE html>
<html lang="en">
<head>
<meta charset="utf-8">
<title>Quorvana Business Card</title>
<link rel="stylesheet" href="https://fonts.googleapis.com/css2?family=Didact+Gothic&family=Mulish:wght@400;700&display=swap">
<style>
  :root {
    --page-bg: #dfe2e3;
    --card-white: #ffffff;
    --brand-light: #4dd0f4;
    --brand-deep: #2a7ffb;
    --accent: #4ecbf2;
    --text-dark: #3d3d3d;
    --text-mid: #555a5e;
    --shadow: rgba(60, 70, 80, 0.28);
  }
  * { margin: 0; padding: 0; box-sizing: border-box; }
  html, body {
    width: 1200px;
    height: 759px;
    overflow: hidden;
    background: var(--page-bg);
  }
  .stage {
    position: relative;
    width: 1200px;
    height: 759px;
  }
  .card {
    position: absolute;
    box-shadow: 6px 6px 8px var(--shadow);
    overflow: hidden;
  }
  .card-front {
    left: 159px;
    top: 270px;
    width: 397px;
    height: 229px;
    background: linear-gradient(90deg, var(--brand-light) 0%, var(--brand-light) 18%, var(--brand-deep) 100%);
    display: flex;
    align-items: center;
    justify-content: center;
  }
  .wordmark {
    font-family: "Didact Gothic", sans-serif;
    font-weight: 400;
    letter-spacing: 1px;
    line-height: 1;
  }
  .card-front .wordmark {
    color: var(--card-white);
    font-size: 47px;
    margin-top: -4px;
  }
  .card-back {
    left: 681px;
    top: 181px;
    width: 227px;
    height: 396px;
    background: var(--card-white);
  }
  .card-back .wordmark {
    position: absolute;
    left: 27px;
    top: 28px;
    color: var(--accent);
    font-size: 37px;
  }
  .accent-bar {
    position: absolute;
    left: 0;
    top: 137px;
    width: 9px;
    height: 28px;
    background: var(--accent);
  }
  .holder {
    position: absolute;
    left: 27px;
    top: 134px;
    font-family: "Mulish", sans-serif;
  }
  .holder-name {
    font-weight: 700;
    font-size: 14px;
    color: var(--accent);
    line-height: 18px;
  }
  .holder-title {
    font-weight: 400;
    font-size: 14px;
    color: var(--text-dark);
    line-height: 18px;
  }
  .contact-list {
    position: absolute;
    left: 27px;
    top: 198px;
    list-style: none;
    font-family: "Mulish", sans-serif;
    font-size: 13px;
    color: var(--text-mid);
  }
  .contact-list li {
    display: flex;
    align-items: center;
    height: 18px;
  }
  .icon {
    width: 10px;
    height: 10px;
    margin-right: 14px;
    flex: none;
    fill: var(--accent);
  }
  .address-band {
    position: absolute;
    left: 0;
    bottom: 0;
    width: 227px;
    height: 87px;
    background: linear-gradient(90deg, var(--brand-light) 0%, var(--brand-deep) 100%);
  }
  .address {
    position: absolute;
    left: 27px;
    top: 22px;
    display: flex;
    font-family: "Mulish", sans-serif;
    font-size: 13px;
    line-height: 19px;
    color: var(--card-white);
    font-style: normal;
  }
  .address .icon {
    fill: var(--card-white);
    height: 12px;
    margin-top: 1px;
    margin-right: 15px;
  }
</style>
</head>
<body>
<main class="stage">
  <section class="card card-front" aria-label="Card front">
    <span class="wordmark">quorvana</span>
  </section>

  <section class="card card-back" aria-label="Card back">
    <span class="wordmark">quorvana</span>
    <span class="accent-bar"></span>
    <div class="holder">
      <p class="holder-name">Dale Fenwick</p>
      <p class="holder-title">President</p>
    </div>
    <ul class="contact-list">
      <li>
        <svg class="icon" viewBox="0 0 10 10" aria-hidden="true"><path d="M2 0.5 L3.6 2.6 L2.7 3.6 C3.3 5 4.9 6.6 6.4 7.3 L7.4 6.4 L9.5 8 L8.5 9.5 C4.5 9.3 0.7 5.5 0.5 1.5 Z"/></svg>
        (800) 417-2964
      </li>
      <li>
        <svg class="icon" viewBox="0 0 10 10" aria-hidden="true"><path d="M0.5 2 H9.5 V8 H0.5 Z M0.5 2.4 L5 5.4 L9.5 2.4" fill-rule="evenodd"/><path d="M0.9 2.6 L5 5.6 L9.1 2.6" stroke="#fff" stroke-width="0.9" fill="none"/></svg>
        sleep@quorvana.com
      </li>
      <li>
        <svg class="icon" viewBox="0 0 10 10" aria-hidden="true"><circle cx="5" cy="5" r="4.5"/><path d="M0.5 5 H9.5 M5 0.5 C2.8 3 2.8 7 5 9.5 M5 0.5 C7.2 3 7.2 7 5 9.5 M1.3 2.8 H8.7 M1.3 7.2 H8.7" stroke="#fff" stroke-width="0.7" fill="none"/></svg>
        www.quorvana.com
      </li>
    </ul>
    <div class="address-band">
      <address class="address">
        <svg class="icon" viewBox="0 0 10 12" aria-hidden="true"><path d="M5 0 C2.2 0 0.5 2 0.5 4.3 C0.5 7.2 5 12 5 12 C5 12 9.5 7.2 9.5 4.3 C9.5 2 7.8 0 5 0 Z M5 2.6 A1.7 1.7 0 1 0 5 6 A1.7 1.7 0 1 0 5 2.6 Z" fill-rule="evenodd"/></svg>
        <span>14 Harwell Street,<br>Lindmoor NSW 2071</span>
      </address>
    </div>
  </section>
</main>
</body>
</html>
```